Cosmetic injections clinic needs a fresh looking business card

We need a business card using the supplied logo and color scheme to attract future clients to our clinic. It should be modern and fresh, eye catching and not too busy. Simple and to the point is best. I would like two sided designs with the front indicating address and contact information, and the back in full color with white logo and descriptive information also provided.
Target Market(s)
Clients looking for non surgical beauty enhancements.
Contact Information for Business Card
MeloraSkin
14, 618 Birchmont Way
St. Albert, Alberta
K2P 7W3
Phone: 587-412-6630
Email: info@meloraskin.com
Requirements
Must have
- -Logo supplied with the name and address of the clinic
- -Back of card in full color with white logo with A small line of text indicating both of the following: Anti aging consultants and cosmetic injectables
- Located inside the Voyager Wellness Group

```html
<!DOCTYPE html>
<html lang="en">
<head>
<meta charset="utf-8">
<title>MeloraSkin Business Card</title>
<link href="https://fonts.googleapis.com/css2?family=Roboto:wght@400;500;700&display=swap" rel="stylesheet">
<style>
  :root {
    --backdrop: #2b2b2b;
    --card-light: #f1f1f1;
    --purple: #6b479c;
    --pink: #e2439a;
    --white: #ffffff;
  }
  html, body {
    margin: 0;
    width: 1200px;
    height: 960px;
    overflow: hidden;
    background: var(--backdrop);
    font-family: "Roboto", Arial, sans-serif;
  }
  .canvas { position: relative; width: 1200px; height: 960px; }
  .card {
    position: absolute;
    width: 598px;
    height: 342px;
    border-radius: 18px;
    overflow: hidden;
    box-shadow: 0 4px 8px rgba(0,0,0,.45);
  }
  .card-front { left: 322px; top: 108px; background: var(--card-light); }
  .card-back { left: 320px; top: 493px; background: var(--pink); }
  .wave { position: absolute; inset: 0; }
  .brand {
    position: absolute;
    display: flex;
    align-items: center;
    gap: 12px;
    font-weight: 700;
  }
  .brand-dot { border-radius: 50%; flex: none; }
  .front-brand { left: 48px; top: 98px; color: var(--purple); font-size: 44px; }
  .front-brand .brand-dot { width: 30px; height: 30px; background: var(--purple); }
  .contact {
    position: absolute;
    right: 28px;
    top: 146px;
    text-align: right;
    color: var(--white);
    font-size: 14px;
    line-height: 18px;
  }
  .person-name { color: var(--pink); font-size: 19px; font-weight: 500; line-height: 22px; }
  .person-role { font-size: 14px; font-weight: 500; margin-bottom: 10px; }
  .address { margin-bottom: 10px; }
  .contact-row { display: flex; justify-content: flex-end; align-items: center; gap: 8px; height: 19px; }
  .contact-row svg { width: 12px; height: 12px; fill: var(--pink); }
  .back-brand {
    left: 0; right: 0; top: 118px;
    justify-content: center;
    color: var(--white);
    font-size: 52px;
  }
  .back-brand .brand-dot { width: 36px; height: 36px; background: var(--white); }
  .tagline {
    position: absolute;
    left: 0; right: 0; top: 268px;
    text-align: center;
    color: var(--white);
    font-size: 14px;
    line-height: 18px;
  }
  .tagline-rule { width: 310px; height: 1px; background: var(--white); margin: 4px auto 4px; }
</style>
</head>
<body>
<div class="canvas">
  <section class="card card-front">
    <svg class="wave" viewBox="0 0 598 342" aria-hidden="true">
      <path d="M598,40 C515,40 470,90 395,172 C325,250 230,326 98,342 L598,342 Z" fill="var(--pink)"/>
      <path d="M598,45 C522,45 480,95 408,175 C338,252 245,330 113,342 L598,342 Z" fill="var(--purple)" stroke="var(--white)" stroke-width="2"/>
    </svg>
    <div class="brand front-brand"><span class="brand-dot"></span>MeloraSkin</div>
    <div class="contact">
      <div class="person-name">DANIEL REYES</div>
      <div class="person-role">CEO/FOUNDER</div>
      <div class="address">MeloraSkin<br>14, 618 Birchmont Way<br>St. Albert, Alberta, K2P 7W3</div>
      <div class="contact-row">587-412-6630
        <svg viewBox="0 0 24 24"><path d="M6.6 10.8a15 15 0 0 0 6.6 6.6l2.2-2.2c.3-.3.7-.4 1-.2 1.1.4 2.3.6 3.6.6.6 0 1 .4 1 1V20c0 .6-.4 1-1 1A17 17 0 0 1 3 4c0-.6.4-1 1-1h3.5c.6 0 1 .4 1 1 0 1.3.2 2.5.6 3.6.1.3 0 .7-.2 1z"/></svg>
      </div>
      <div class="contact-row">info@meloraskin.com
        <svg viewBox="0 0 24 24"><path d="M2 5h20v14H2z M2 5l10 7 10-7" stroke="var(--purple)" stroke-width="1.5"/></svg>
      </div>
      <div class="contact-row">meloraskin.com
        <svg viewBox="0 0 24 24"><circle cx="12" cy="12" r="10"/><path d="M2 12h20M12 2c3 3 3 17 0 20M12 2c-3 3-3 17 0 20" stroke="var(--purple)" stroke-width="1.5" fill="none"/></svg>
      </div>
    </div>
  </section>

  <section class="card card-back">
    <div class="brand back-brand"><span class="brand-dot"></span>MeloraSkin</div>
    <div class="tagline">
      Anti aging consultants &amp; cosmetic injectables
      <div class="tagline-rule"></div>
      Located inside the Voyager Wellness Group
    </div>
  </section>
</div>
</body>
</html>
```